VL Profile

Design a professional company profile using stock images and images supplied. Use industry related images from Electrical and Mechanical Engineering
Target Market(s)
Businesses
Industry/Entity Type
Electrical, Mechanical
Requirements
Must have
- Company Logo Colors
Nice to have
- Professional Look and feel

```html
<!DOCTYPE html>
<html lang="en">
<head>
<meta charset="utf-8">
<title>VL Profile – Velani Projects</title>
<link href="https://fonts.googleapis.com/css2?family=Montserrat:wght@500;600;700;800&family=Open+Sans:wght@400;600;700&display=swap" rel="stylesheet">
<style>
:root{
  --bg:#3c3c3c;
  --navy:#1b3f8e;
  --navy-deep:#142f6e;
  --bright:#1e6fc6;
  --label:#1565c0;
  --sky:#4a8ed8;
  --ink:#1d1d1f;
  --grey:#6c6c6c;
  --grey-light:#d5d5d5;
  --gold:#d8b94c;
  --white:#ffffff;
  --black:#000000;
}
*{box-sizing:border-box;margin:0;padding:0}
html,body{width:1200px;height:2978px;overflow:hidden}
body{background:var(--bg);font-family:"Open Sans",Arial,sans-serif;position:relative;color:var(--ink)}
.page{position:absolute;width:506px;height:656px;overflow:hidden;background:var(--white)}
.col-l{left:76px}.col-r{left:619px}
.row1{top:98px}.row2{top:809px}.row3{top:1519px}.row4{top:2230px}
.abs{position:absolute}
.photo{position:absolute}
.label{position:absolute;background:var(--label);color:var(--white);font:700 12.5px/1 "Open Sans",sans-serif;text-transform:uppercase;display:flex;align-items:center;padding-left:12px;letter-spacing:.2px}
.label.outline{background:none;border:1.5px solid var(--white);justify-content:center;padding:0}
.body-text{position:absolute;font-size:8.4px;line-height:10.8px}
.body-text p{margin-bottom:9px}
.body-text ul{list-style:none}
.body-text li::before{content:"• "}
.white{color:var(--white)}
.brand{position:absolute;display:flex;flex-direction:column;align-items:center;font-family:"Montserrat",sans-serif;font-weight:600;color:var(--navy)}
.brand .mark{width:34px;height:34px;border:3px solid currentColor;border-radius:50%;margin-bottom:12px}
.brand .name{font-size:25px;letter-spacing:6px;line-height:1}
.brand .sub{font-size:10px;letter-spacing:4px;margin-top:5px}
.brand.light{color:var(--white)}

.contact-us{position:absolute;left:11px;top:431px;width:248px;height:38px;background:var(--grey);color:var(--white);font:600 23px/38px "Montserrat",sans-serif;letter-spacing:5px;padding-left:15px}
.contact-list{position:absolute;left:290px;top:494px;list-style:none;font:600 14.5px/20px "Open Sans",sans-serif;color:var(--navy-deep)}
.contact-list li{display:flex;gap:8px;align-items:flex-start}
.contact-list svg{flex:none;margin-top:5px}

.cover-title{position:absolute;left:12px;color:var(--white);font:600 25px/1 "Montserrat",sans-serif;letter-spacing:.3px}

.who-top{position:absolute;left:0;top:0;width:506px;height:316px;background:var(--navy)}
.who-title{position:absolute;left:234px;top:151px;width:252px;height:36px;background:var(--navy-deep);color:var(--gold);font:600 25px/36px "Montserrat",sans-serif;letter-spacing:5px;text-align:center}
.mission{position:absolute;left:0;top:316px;width:188px;height:340px;background:var(--white)}
.services{position:absolute;left:188px;top:316px;width:318px;height:340px;background:var(--black)}
.services-title{position:absolute;left:51px;top:25px;width:211px;height:24px;border:1.5px solid var(--label);color:var(--white);font:700 12px/21px "Montserrat",sans-serif;letter-spacing:4px;text-align:center}
.svc{position:absolute;width:90px;margin-left:-45px;text-align:center;color:var(--white);font:600 7.2px/8.4px "Open Sans",sans-serif;text-transform:uppercase}
.svc svg{display:block;margin:0 auto 5px}
.objectives{list-style:none;font-size:8.2px;line-height:10.6px}
.objectives li{position:relative;padding-left:14px;margin-bottom:10px}
.objectives li::before{content:"";position:absolute;left:2px;top:2px;width:5px;height:5px;border-top:1.5px solid var(--label);border-right:1.5px solid var(--label);transform:rotate(45deg)}

.band-black{position:absolute;left:0;width:506px;background:var(--black);color:var(--white);font:700 9.4px/11.5px "Open Sans",sans-serif;text-align:center;text-transform:uppercase;display:flex;align-items:center;justify-content:center}
.band{position:absolute;left:0;width:506px}
.framed{position:absolute;border:3px solid var(--white)}
.projects-title{position:absolute;left:251px;top:24px;font:800 45px/1 "Montserrat",sans-serif;color:var(--navy)}
.clients{position:absolute;left:38px;top:18px;font:700 9px/11.5px "Open Sans",sans-serif;color:var(--ink);text-transform:uppercase;width:180px}
.logo-slot{position:absolute;top:20px;width:60px;height:60px;background:#d9d9d9;color:var(--ink);font:600 8px/60px "Open Sans",sans-serif;text-align:center}
</style>
</head>
<body>

<section class="page col-l row1">
  <div class="photo" style="left:0;top:0;width:506px;height:418px;background:linear-gradient(160deg,#27478f,#1a3777 60%,#203f86)" role="img" aria-label="Office building facade with stone tower, tinted blue"></div>
  <svg class="abs" style="left:0;top:0" width="506" height="418">
    <polygon points="0,0 146,0 0,166" fill="#6a6a6a"/>
    <polygon points="307,0 506,0 506,136" fill="#ffffff"/>
  </svg>
  <div class="contact-us">CONTACT US</div>
  <div class="brand" style="left:30px;top:502px;width:220px">
    <span class="mark"></span>
    <span class="name">VELANI</span>
    <span class="sub">PROJECTS</span>
  </div>
  <ul class="contact-list">
    <li><svg width="11" height="13" viewBox="0 0 11 13"><path d="M5.5 0C2.5 0 0 2.4 0 5.3 0 9 5.5 13 5.5 13S11 9 11 5.3C11 2.4 8.5 0 5.5 0z" fill="#142f6e"/><circle cx="5.5" cy="5.2" r="2" fill="#fff"/></svg><span>Unit B, 12 Acacia Lane,<br>Rivonia, Sandton 2128</span></li>
    <li><svg width="11" height="11" viewBox="0 0 11 11"><path d="M2 0l2 2.8-1.2 1.4c.7 1.6 2.2 3.1 3.8 3.8L8 6.8 11 9l-1.5 2C4.5 10.8.2 6.5 0 1.5z" fill="#142f6e"/></svg><span>010 555 0147</span></li>
    <li><svg width="11" height="9" viewBox="0 0 11 9"><rect width="11" height="9" fill="#142f6e"/><path d="M0 0l5.5 4.5L11 0" stroke="#fff" fill="none"/></svg><span>info@velaniprojects.co.za</span></li>
    <li><svg width="11" height="11" viewBox="0 0 11 11"><circle cx="5.5" cy="5.5" r="4.8" stroke="#142f6e" fill="none"/><path d="M.7 5.5h9.6M5.5.7c-2.5 3-2.5 6.6 0 9.6M5.5.7c2.5 3 2.5 6.6 0 9.6" stroke="#142f6e" fill="none"/></svg><span>www.velaniprojects.co.za</span></li>
  </ul>
</section>

<section class="page col-r row1">
  <div class="brand" style="left:103px;top:20px;width:300px">
    <span class="mark" style="width:46px;height:46px;margin-bottom:30px"></span>
    <span class="name" style="font-size:30px;letter-spacing:8px">VELANI</span>
    <span class="sub" style="font-size:13px;letter-spacing:5px">PROJECTS</span>
  </div>
  <svg class="abs" style="left:0;top:0" width="506" height="656">
    <defs>
      <linearGradient id="gears" x1="0" y1="0" x2="1" y2="1">
        <stop offset="0" stop-color="#3d5fa6"/><stop offset=".5" stop-color="#23458f"/><stop offset="1" stop-color="#193674"/>
      </linearGradient>
      <linearGradient id="worker" x1="0" y1="0" x2="1" y2="1">
        <stop offset="0" stop-color="#f4f1ec"/><stop offset=".6" stop-color="#d9d2c6"/><stop offset="1" stop-color="#c9b37a"/>
      </linearGradient>
    </defs>
    <polygon points="250,150 506,150 506,420 420,568 250,394" fill="url(#worker)" role="img" aria-label="Smiling electrician in overalls holding a cable coil and giving a thumbs up"/>
    <polygon points="506,420 506,656 420,568" fill="#6b6b6b"/>
    <polygon points="0,138 506,656 0,656" fill="url(#gears)" role="img" aria-label="Electrical switchboard and mechanical gears, tinted blue"/>
    <line x1="0" y1="138" x2="506" y2="656" stroke="#1a50a8" stroke-width="12"/>
  </svg>
  <div class="cover-title" style="top:428px">ELECTRICAL</div>
  <div class="cover-title" style="top:620px">MECHANICAL ENGINEERING</div>
</section>

<section class="page col-l row2">
  <div class="who-top"></div>
  <div class="photo" style="left:18px;top:14px;width:309px;height:161px;background:linear-gradient(120deg,#c9b86a,#a8895f 45%,#7b7062)" role="img" aria-label="Company office building with stone tower entrance"></div>
  <div class="brand light" style="left:339px;top:28px;width:151px">
    <span class="mark" style="width:30px;height:30px;margin-bottom:12px"></span>
    <span class="name" style="font-size:17px;letter-spacing:4px">VELANI</span>
    <span class="sub" style="font-size:7.5px;letter-spacing:3px;margin-top:3px">PROJECTS</span>
  </div>
  <div class="who-title">WHO WE ARE</div>
  <div class="body-text white" style="left:18px;top:202px;width:470px;text-align:justify">
    Established in 2013, Velani Projects (Pty) Ltd. is based in Rivonia, Johannesburg, South Africa. Velani Projects specialises in electrical and mechanical services in the residential, commercial and industrial sectors. We have extensive experience in projects with a value of works contracts. We believe that promoting our business is developing good working relationships with our clients. To this end, we aim to provide high-quality workmanship, on time and within budget. We endeavour to earn the trust and confidence of our clients by being reliable and transparent. Our reliability and excellence have gained us a good reputation and have resulted in repeat business from many satisfied clients. We are committed to quality, health &amp; safety, training and environmental issues. We review and continually improve our practices, to drive improvements in environmental, health, safety, and security excellence in all our projects.
  </div>

  <div class="mission">
    <div class="label" style="left:0;top:25px;width:174px;height:23px">Mission Statement</div>
    <div class="body-text" style="left:24px;top:56px;width:154px">Our mission is to give our customers satisfaction in all our services. We obtain complete customer specifications and job requirements at the time of the quotation or tender, before the commencement of the contract or work order.</div>
    <div class="label" style="left:0;top:150px;width:174px;height:23px">Our Objectives</div>
    <ul class="objectives" style="position:absolute;left:10px;top:182px;width:170px">
      <li>Create a service that aims to meet and exceed customers' expectations with quality products and workmanship.</li>
      <li>Continue to establish as a reliable leader in the highest quality workmanship.</li>
      <li>Maintain excellence in workmanship and relations with our present and future clients.</li>
    </ul>
  </div>

  <div class="services">
    <div class="services-title">OUR SERVICES</div>
    <div class="svc" style="left:78px;top:68px"><svg width="50" height="50" viewBox="0 0 50 50"><circle cx="25" cy="25" r="23" fill="#d6e7f8" stroke="#fff" stroke-width="3"/><circle cx="25" cy="25" r="13" fill="none" stroke="#1565c0" stroke-width="2.5"/><path d="M21 18v6M29 18v6M19 24h12v4a6 6 0 0 1-12 0z M25 34v5" fill="none" stroke="#1565c0" stroke-width="2.5"/></svg>Electrical<br>Installations</div>
    <div class="svc" style="left:159px;top:68px"><svg width="50" height="50" viewBox="0 0 50 50"><circle cx="25" cy="25" r="23" fill="#d6e7f8" stroke="#fff" stroke-width="3"/><circle cx="25" cy="25" r="13" fill="none" stroke="#1565c0" stroke-width="2.5"/><path d="M27 15l-6 11h5l-3 9 7-12h-5z" fill="#1565c0"/></svg>Electrical<br>Maintenance</div>
    <div class="svc" style="left:239px;top:68px"><svg width="50" height="50" viewBox="0 0 50 50"><circle cx="25" cy="25" r="23" fill="#d6e7f8" stroke="#fff" stroke-width="3"/><path d="M15 15l20 20M35 15L15 35" stroke="#1565c0" stroke-width="3.5" stroke-linecap="round"/></svg>Instrumentation</div>

    <div class="svc" style="left:46px;top:146px"><svg width="46" height="46" viewBox="0 0 50 50"><circle cx="25" cy="25" r="23" fill="#d6e7f8" stroke="#fff" stroke-width="3"/><path d="M25 11v19" stroke="#1565c0" stroke-width="5" stroke-linecap="round"/><circle cx="25" cy="38" r="3" fill="#1565c0"/></svg>Fault<br>Finding</div>
    <div class="svc" style="left:120px;top:146px"><svg width="46" height="46" viewBox="0 0 50 50"><circle cx="25" cy="25" r="23" fill="#d6e7f8" stroke="#fff" stroke-width="3"/><rect x="17" y="13" width="16" height="24" rx="2" fill="none" stroke="#1565c0" stroke-width="2.5"/><rect x="20" y="16" width="10" height="6" fill="#1565c0"/><circle cx="25" cy="30" r="3" fill="none" stroke="#1565c0" stroke-width="2"/></svg>Testing</div>
    <div class="svc" style="left:196px;top:146px"><svg width="46" height="46" viewBox="0 0 50 50"><circle cx="25" cy="25" r="23" fill="#d6e7f8" stroke="#fff" stroke-width="3"/><circle cx="25" cy="25" r="13" fill="none" stroke="#1565c0" stroke-width="2.5"/><path d="M18 26l5 5 9-12" fill="none" stroke="#1565c0" stroke-width="2.5"/></svg>Rooting</div>
    <div class="svc" style="left:274px;top:146px"><svg width="46" height="46" viewBox="0 0 50 50"><circle cx="25" cy="25" r="23" fill="#d6e7f8" stroke="#fff" stroke-width="3"/><rect x="12" y="17" width="26" height="11" rx="2" fill="none" stroke="#1565c0" stroke-width="2.5"/><path d="M17 32v4M23 32v4M29 32v4M35 32v4" stroke="#1565c0" stroke-width="2"/></svg>HVAC<br>Systems</div>

    <div class="svc" style="left:78px;top:230px"><svg width="46" height="46" viewBox="0 0 50 50"><circle cx="25" cy="25" r="23" fill="#d6e7f8" stroke="#fff" stroke-width="3"/><rect x="15" y="16" width="20" height="18" fill="none" stroke="#1565c0" stroke-width="2.5"/><path d="M15 22h20M15 28h20M22 16v18M28 16v18" stroke="#1565c0" stroke-width="1.5"/></svg>Solar &amp; Battery<br>Backup Solutions</div>
    <div class="svc" style="left:159px;top:230px"><svg width="46" height="46" viewBox="0 0 50 50"><circle cx="25" cy="25" r="23" fill="#d6e7f8" stroke="#fff" stroke-width="3"/><path d="M25 12l13 24H12z" fill="none" stroke="#1565c0" stroke-width="2.5"/><path d="M26 19l-4 8h4l-2 6" fill="none" stroke="#1565c0" stroke-width="2"/></svg>High Voltage<br>&amp; Substations</div>
    <div class="svc" style="left:239px;top:230px"><svg width="46" height="46" viewBox="0 0 50 50"><circle cx="25" cy="25" r="23" fill="#d6e7f8" stroke="#fff" stroke-width="3"/><rect x="16" y="13" width="16" height="22" fill="none" stroke="#1565c0" stroke-width="2.5"/><path d="M19 19h10M19 24h10" stroke="#1565c0" stroke-width="2"/><circle cx="31" cy="33" r="5" fill="#1565c0"/></svg>Certificates<br>of Compliance</div>
  </div>
</section>

<section class="page col-r row2">
  <div class="abs" style="left:0;top:0;width:506px;height:145px;background:var(--bright)"></div>
  <div class="photo" style="left:16px;top:22px;width:169px;height:111px;background:linear-gradient(135deg,#d9c36a,#8b8a86 50%,#3a3c44)" role="img" aria-label="Hands wiring a distribution board"></div>
  <div class="label outline" style="left:202px;top:22px;width:206px;height:24px">Electrical Installation</div>
  <div class="body-text white" style="left:202px;top:54px;width:286px;text-align:justify">The fixed electrical installation is the electrical wiring, electrical machinery and electrical components that are fixed to a building. Installations include, for instance, fuse boxes, solar or generator installations, ceiling lights, power sockets, and large items of machinery termination. Velani Projects will plan and design, select and install, commission, test, report, maintain, fault find and repair systems to a high standard.</div>

  <div class="label" style="left:18px;top:158px;width:209px;height:23px;background:var(--black)">Electrical Maintenance</div>
  <div class="body-text" style="left:18px;top:190px;width:472px">
    <p>Electrical maintenance involves fixing any sort of electrical device should it become out of order or suffer a break-down (repair, unscheduled, or casualty maintenance). This service includes the tightening of all electrical connections and upgrading the power rating of safety switches.</p>
    <p>Electrical maintenance also means anticipating and planning through the provision of regular care plans or preventative maintenance schedules and checklists of electrical equipment/instruments to avoid any breakdown or fault. Velani Projects offers electrical maintenance services at industrial, commercial and residential levels. These services include:</p>
    <ul style="margin-bottom:9px">
      <li>Electrical re-wiring of houses, office blocks and industries</li>
      <li>Fault finding and repair of fault</li>
      <li>Repair of faulty lights, switches and plugs</li>
      <li>Repair of tripping switches</li>
      <li>Assist with power supply issues</li>
      <li>General electrical-related repairs</li>
      <li>Connection of hot water systems (geyser etc.)</li>
      <li>Maintenance and servicing of Heating, Ventilation and Air Conditioning systems</li>
      <li>Electrical reticulation</li>
    </ul>
    <p>Velani Projects provides premier electrical contracting and maintenance for the public sector, business, and private customers in commercial, domestic and industrial markets throughout South Africa. We offer short and long-term maintenance contracts.</p>
  </div>
  <div class="photo" style="left:17px;top:448px;width:297px;height:198px;background:linear-gradient(110deg,#c7cdd4,#9aa1a8 40%,#d9c07a 70%,#6f6a60)" role="img" aria-label="Electrician in hard hat working on a control panel"></div>
  <div class="abs" style="left:314px;top:448px;width:182px;height:198px;background:var(--navy)"></div>
  <div class="label outline" style="left:328px;top:459px;width:158px;height:23px">Fault Finding</div>
  <div class="body-text white" style="left:334px;top:491px;width:156px">
    <p>Fault Finding is investigating the cause of malfunction in machinery, especially electronic equipment. The following are typical faults that are the most common causes of a circuit ceasing to operate correctly:</p>
    <ul>
      <li>Loss of supply</li><li>Earth fault</li><li>Dead short</li><li>Correct protective device in place</li><li>Defective components</li><li>Breakdown of control circuits</li>
    </ul>
  </div>
</section>

<section class="page col-l row3">
  <div class="abs" style="left:0;top:0;width:196px;height:656px;background:var(--black)"></div>
  <div class="photo" style="left:0;top:25px;width:182px;height:124px;background:linear-gradient(120deg,#f2f2f2,#e4e4e4 50%,#c44a4a 80%,#efefef)" role="img" aria-label="Digital multimeter, test leads and circuit breakers"></div>
  <div class="label" style="left:0;top:178px;width:91px;height:21px">Testing</div>
  <div class="body-text white" style="left:21px;top:219px;width:166px">
    <p>Electrical testing is an essential task and can be time-consuming and inconvenient as the power has to be turned off for some tests. We can generally work around your power requirements in the office, home, or workplace.</p>
    <p>The inspection provides the ideal opportunity for checking the general condition of the equipment and that all parts are in sound condition. Our skilled team provides a comprehensive testing and inspection service, ensuring everything runs as safely and efficiently as possible.</p>
    <p>A periodic inspection will reveal if any electrical equipment is being overloaded, locate any potential electrical shock risks and fire hazards in an installation, identify any defective electrical work, or highlight any lack of earthing or bonding.</p>
  </div>
  <div class="label" style="left:0;top:520px;width:91px;height:21px">Rooting</div>
  <div class="body-text white" style="left:21px;top:569px;width:166px">Our competent installers will gladly execute a high level of workmanship on all rooting to maintain a high level of structural work, and help you choose the rooting system that's just right for you.</div>

  <div class="label" style="left:257px;top:13px;width:181px;height:23px;justify-content:center;padding:0">Instrumentation</div>
  <div class="body-text" style="left:211px;top:44px;width:284px">
    <p>In our instrumentation, we are more focused on the operation instruments and systems that are used in the design and configuration of automated systems.</p>
    <p style="margin-bottom:0">Velani Projects offers the following instrumentation services:</p>
    <ul>
      <li>Automation</li><li>Control Systems</li><li>Instrumentation</li><li>Design and Drawing</li><li>Programmable Logic Control (PLC)</li><li>Software Development</li><li>Process Automation</li><li>Electrical - Heavy and Light Current</li>
      <li style="padding-left:8px">o Motor Control Centre (MCC)</li><li style="padding-left:8px">o Panel Building and Installation</li><li style="padding-left:8px">o Maintenance and Supply</li>
    </ul>
  </div>

  <div class="abs" style="left:196px;top:233px;width:310px;height:423px;background:var(--sky)"></div>
  <div class="photo" style="left:296px;top:245px;width:108px;height:120px;background:linear-gradient(180deg,#2c3f78 0 45%,#c7d6ea 45% 100%)" role="img" aria-label="Solar panel street light"></div>
  <div class="label" style="left:209px;top:382px;width:276px;height:22px;justify-content:center;padding:0">Solar &amp; Battery Backup Solutions</div>
  <div class="body-text white" style="left:211px;top:413px;width:282px;text-align:justify">
    <p>Solar power is currently one of the most secure source of energy for the future. Solar power is the conversion of sunlight into electricity, either directly using photovoltaics (PV), or indirectly using concentrated solar power (CSP). Photovoltaics convert light into an electric current using the photovoltaic effect. PV were initially solely used as a source of electricity for small and medium sized applications, from the calculator powered by a single solar cell to remote homes powered by an off-grid rooftop PV system. As the cost of solar electricity has fallen and competing products become available, the number of grid-connected solar PV systems has grown into the millions and utility scale solar power stations with hundreds of megawatts are being built.</p>
    <p>Velani Projects' competent installers will gladly advise you on all alternative energy technology matters, help you choose the system that's just right for you and after the installation will offer a comprehensive service. Should solar not be your preference, we can also assist you in selecting the best alternative battery backup solution; and advise you on the latest alternative sources of energy available in the market.</p>
  </div>
</section>

<section class="page col-r row3">
  <div class="photo" style="left:13px;top:41px;width:215px;height:141px;background:linear-gradient(180deg,#b9c2cc,#7d858e 55%,#8a7b62)" role="img" aria-label="High voltage substation with transformers"></div>
  <div class="label" style="left:230px;top:42px;width:234px;height:21px">High Voltage &amp; Substations</div>
  <div class="body-text" style="left:245px;top:72px;width:245px">
    <p>Velani Projects offers the following services for High Voltage and Substations:</p>
    <ul>
      <li>High 33KV, Medium 11 KV and Low voltage 600V<br>&nbsp;&nbsp;breakers maintenance and repair</li>
      <li>Protection Relay Testing and upgrade installation</li>
      <li>Transformer Maintenance</li>
      <li>Generator maintenance</li>
      <li>Retrofit Solutions for various breakers.</li>
    </ul>
  </div>
  <div class="photo" style="left:0;top:233px;width:506px;height:173px;background:radial-gradient(ellipse at 52% 50%,#3f86d8,#163a86 55%,#0d2256)" role="img" aria-label="Hand holding glowing compliance graphic with regulations, policies and standards"></div>
  <div class="abs" style="left:0;top:406px;width:506px;height:250px;background:var(--navy)"></div>
  <div class="label outline" style="left:125px;top:420px;width:234px;height:23px">Certificates of Compliance</div>
  <div class="body-text white" style="left:28px;top:454px;width:456px">
    <p>A Certificate of Compliance is a certificate issued by a registered person regarding an electrical installation or part of an electrical installation; or issued under the Electrical Installation Regulations, 1992.</p>
    <p>Velani Projects keeps informed on the latest legislation requirements by the Electrical Contractors Board and Association, as well as the provincial Electrical Inspectorate, to ensure we deliver the most accurate Electrical Compliance Certificate possible to our clients.</p>
    <p style="margin-bottom:0">Our Master Installer issues COC's for buildings and projects such as:</p>
    <ul>
      <li>Hospitals</li><li>Petrol stations</li><li>Hazardous environments</li><li>Laboratories</li><li>Shopping malls</li><li>Factories and warehouses</li><li>All AC and DC installations</li><li>Any and all industrial, commercial and domestic electrical installations</li>
    </ul>
  </div>
</section>

<section class="page col-l row4">
  <div class="brand" style="left:30px;top:12px;width:128px">
    <span class="mark" style="width:26px;height:26px;border-width:2.5px;margin-bottom:10px"></span>
    <span class="name" style="font-size:15px;letter-spacing:3px">VELANI</span>
    <span class="sub" style="font-size:6.5px;letter-spacing:2px;margin-top:3px">PROJECTS</span>
  </div>
  <div class="projects-title">PROJECTS</div>
  <div class="band-black" style="top:101px;height:36px">Subcontracted: Tesselate Technologies for electrical installation of<br>Karoo Ridge Industrial Park CCTV system to cover internal roads - 2021</div>
  <div class="band" style="top:137px;height:225px;background:var(--grey-light)"></div>
  <div class="framed photo" style="left:23px;top:164px;width:187px;height:162px;background:linear-gradient(160deg,#8f9aa6,#8b7a5c 55%,#6f6650)" role="img" aria-label="CCTV camera pole on site"></div>
  <div class="framed photo" style="left:216px;top:164px;width:268px;height:162px;background:linear-gradient(170deg,#9aa5ad,#7c7f76 45%,#8c7b5f)" role="img" aria-label="Aerial view of industrial park roofs"></div>
  <div class="band-black" style="top:362px;height:36px">Subcontractor: Supply and installation of all electrical instruments in raw<br>water pump station, Mbila Dam, Sekgopo District Municipality, Limpopo - 2023</div>
  <div class="band" style="top:398px;height:240px;background:var(--navy)"></div>
  <div class="framed photo" style="left:26px;top:422px;width:124px;height:180px;background:linear-gradient(160deg,#d08a2f,#9a5a1f 60%,#3a2a20)" role="img" aria-label="Orange motor control panels in pump station"></div>
  <div class="framed photo" style="left:156px;top:422px;width:122px;height:180px;background:linear-gradient(170deg,#c9782a,#d7d2c8 55%,#8a6a4a)" role="img" aria-label="Open control panel with wiring"></div>
  <div class="framed photo" style="left:284px;top:422px;width:198px;height:180px;background:linear-gradient(170deg,#a47a5c,#8e8e8a 50%,#5e5e5a)" role="img" aria-label="Pump station interior with pipework"></div>
  <div class="band" style="top:638px;height:18px;background:var(--black)"></div>
</section>

<section class="page col-r row4">
  <div class="clients">Clients<br>• Marula Ridge Properties<br>• Northgate Developers<br>• Tesselate Technologies<br>• Savanna Mutual Bank</div>
  <div class="logo-slot" style="left:228px">LOGO</div>
  <div class="logo-slot" style="left:295px">LOGO</div>
  <div class="logo-slot" style="left:362px">LOGO</div>
  <div class="logo-slot" style="left:429px">LOGO</div>
  <div class="band-black" style="top:101px;height:36px">Electrical contractor: Electrical installation of<br>the refurbished of Old Marsden Building, Bloemfontein, Free State - 2023</div>
  <div class="band" style="top:137px;height:225px;background:var(--navy)"></div>
  <div class="framed photo" style="left:20px;top:164px;width:186px;height:162px;background:linear-gradient(160deg,#8f9aa6,#8b7a5c 55%,#6f6650)" role="img" aria-label="Site view of refurbished building"></div>
  <div class="framed photo" style="left:212px;top:164px;width:268px;height:162px;background:linear-gradient(170deg,#9aa5ad,#7c7f76 45%,#8c7b5f)" role="img" aria-label="Aerial view of building complex"></div>
  <div class="band-black" style="top:362px;height:36px">Electrical contractor: Renovations at<br>48 Hillcrest Ave, Randburg, Johannesburg, Gauteng - 2022</div>
  <div class="band" style="top:398px;height:240px;background:var(--grey-light)"></div>
  <div class="framed photo" style="left:25px;top:426px;width:143px;height:176px;background:linear-gradient(180deg,#3a3630,#6e6254 50%,#2a2622)" role="img" aria-label="Entrance with ceiling downlights at night"></div>
  <div class="framed photo" style="left:174px;top:426px;width:131px;height:176px;background:linear-gradient(180deg,#e8e6e2,#b9b5ae 55%,#5c5750)" role="img" aria-label="Interior staircase with chandelier"></div>
  <div class="framed photo" style="left:311px;top:426px;width:167px;height:176px;background:linear-gradient(180deg,#0d1326,#1a2a4e 55%,#1d5fd0)" role="img" aria-label="House exterior with lit pool at night"></div>
  <div class="band" style="top:638px;height:18px;background:var(--black)"></div>
</section>

</body>
</html>
```